Aquaponic greenhouse needs a business brochure that shows what a unique system we have

We would like to expand our marketing beyond social media. We are a aquaponic greenhouse where we use fish to fertilize the water so that we don't have to use any chemicals in the system. This method is sustainable and environmentally friendly. We grow in a climate controlled system year round and deliver the freshest produce directly to our local families, schools and restaurants. All of our produce is grown from seed, closely monitored during the growing cycle, hand picked and hand packaged for our customers.

Aquaponics - The combination of Aquaculture (raising fish) and Hydroponics (growing plants in a soilless system)

Sustainable - Closed loop system using the same water for the fish and plants.

Local - Delaware natives providing healthy eating opportunities for our neighbors throughout the state.

Chemical and Soil Free

Largest in the First State - With over 15,000 square feet of a climate controlled environment, we can grow the freshest produce year round with consistent output.

Target Market(s)

Customers and those who don’t use social media

Industry/Entity Type

Agribusiness

Font styles to use
Sans Serif

Colors
0255a3
32b8a4
9bcb3c
cadf82

Requirements
Must have
• Our logo (attached) some personalized pictures (can be found on our website www.quillmeadowgrow.com) and areas where we can customize our written content. Must have editable text and be able to replace pictures as we grow.
Nice to have
• Options for a tri-fold and bi-fold brochures

```html
<!DOCTYPE html>
<html lang="en">
<head>
<meta charset="utf-8">
<title>Aquaponics Greenhouse Brochure</title>
<link href="https://fonts.googleapis.com/css2?family=Montserrat:wght@300;400;700;800&display=swap" rel="stylesheet">
<style>
  :root {
    --green-dark: #629c36;
    --green-light: #d4e4ad;
    --leaf-deep: #1f5e2c;
    --leaf-mid: #3f8f45;
    --ink: #1c1c1c;
    --paper: #ffffff;
  }
  * { margin: 0; padding: 0; box-sizing: border-box; }
  html, body { width: 1200px; height: 847px; overflow: hidden; background: var(--paper); }
  .brochure {
    position: relative;
    width: 1200px;
    height: 847px;
    font-family: "Montserrat", sans-serif;
    color: var(--ink);
    overflow: hidden;
  }
  .shapes { position: absolute; inset: 0; width: 1200px; height: 847px; }
  .cover-text {
    position: absolute;
    left: 43px;
    top: 203px;
    width: 302px;
    text-align: center;
    color: var(--paper);
    font-weight: 700;
    text-shadow: 0 1px 3px rgba(0,0,0,.35);
  }
  .cover-title { font-size: 35px; line-height: 40px; font-weight: 800; }
  .cover-sub { font-size: 23.5px; line-height: 34px; }
  .feature-title {
    position: absolute;
    color: var(--green-dark);
    font-weight: 800;
    white-space: nowrap;
  }
  .feature-body {
    position: absolute;
    font-weight: 400;
    white-space: nowrap;
  }
  .sustainable-title { left: 449px; top: 82px; font-size: 47px; }
  .sustainable-body { left: 449px; top: 137px; font-size: 28px; line-height: 37.6px; }
  .local-title { left: 456px; top: 418px; font-size: 47px; }
  .local-body { left: 456px; top: 473px; font-size: 28px; line-height: 37.6px; }
  .chemical-title { left: 800px; width: 374px; top: 336px; font-size: 36px; line-height: 44px; text-align: center; white-space: normal; }
  .largest-title { left: 800px; top: 472px; font-size: 36px; }
  .largest-body { left: 800px; top: 560px; font-size: 25.5px; line-height: 34px; }
</style>
</head>
<body>
<main class="brochure">
  <svg class="shapes" viewBox="0 0 1530 1080" preserveAspectRatio="none" aria-hidden="true">
    <defs>
      <linearGradient id="leafGradient" x1="0" y1="0" x2="1" y2="1">
        <stop offset="0" stop-color="#2f7a3a"/>
        <stop offset="0.5" stop-color="#3f9447"/>
        <stop offset="1" stop-color="#256a33"/>
      </linearGradient>
    </defs>
    <!-- cover panel -->
    <rect x="0" y="0" width="533" height="1080" fill="var(--green-dark)"/>
    <polygon points="0,770 265,942 533,770 533,860 265,1033 0,860" fill="var(--green-light)"/>
    <!-- right panel header chevron -->
    <polygon points="995,0 1530,0 1530,235 1262,63 995,235" fill="var(--green-dark)"/>
    <polygon points="995,235 1262,63 1530,235 1530,328 1262,155 995,328" fill="var(--green-light)"/>
  </svg>

  <svg class="shapes" viewBox="0 0 1530 1080" preserveAspectRatio="none">
    <polygon role="img" aria-label="Photo of fresh green clover leaves" points="0,0 533,0 533,770 265,942 0,770" fill="url(#leafGradient)"/>
    <circle role="img" aria-label="Icon of a globe with a sprouting seedling" cx="1258" cy="318" r="52" fill="#a8dbe3" stroke="#1c1c1c" stroke-width="6"/>
  </svg>

  <section class="cover-text">
    <h1 class="cover-title">Aquaponics</h1>
    <p class="cover-sub">The combination of Aquaculture (rais-<br>ing fish) and Hydro-<br>ponics (growing<br>plants in a soilless<br>system)</p>
  </section>

  <h2 class="feature-title sustainable-title">Sustainable</h2>
  <p class="feature-body sustainable-body">Closed loop<br>system using the<br>same water for the<br>fish and plants.</p>

  <h2 class="feature-title local-title">Local</h2>
  <p class="feature-body local-body">Delaware natives<br>providing healthy<br>eating opportuni-<br>ties for our neigh-<br>bors throughout<br>the state.</p>

  <h2 class="feature-title chemical-title">Chemical and Soil Free</h2>

  <h2 class="feature-title largest-title">Largest in the</h2>
  <p class="feature-body largest-body">First State - With over<br>15,000 square feet of a cli-<br>mate controlled environ-<br>ment, we can grow the<br>freshest produce year<br>round with consistent<br>output.</p>
</main>
</body>
</html>
```